A billboard for Harlow Ridge Construction size 36.5’ x 14.5’

Hi guys. We are purchasing a billboard and are looking for a design (size 36.5’ x 14.5’). Our slogan is "Quality you deserve, service you can count on". The goal of this billboard is brand recognition primarily letting people know we do roofs. Attached are logos that can be used if needed. Not necessarily all of them need to be used.

Target Market(s)

Residents in the local areas needing or thinking about a roof replacement

Industry/Entity Type

Roofing

Requirements
Must have
• Logo and services (roof replacement, gutters, siding, and snow removal)
Nice to have
• take a look at our website for ideas www.harlowridgeconstruction.example

```html
<!DOCTYPE html>
<html lang="en">
<head>
<meta charset="utf-8">
<title>Harlow Ridge Construction Billboard</title>
<link href="https://fonts.googleapis.com/css2?family=Montserrat:wght@500;600;700;800&display=swap" rel="stylesheet">
<style>
  :root {
    --page: #e9ebef;
    --white: #ffffff;
    --paper: #f4f4f5;
    --ink: #111111;
    --red: #e41e26;
    --badge-blue: #1b6f96;
    --badge-grey: #b9bcc0;
    --badge-dark: #2b2b2b;
    --wood: #b8823f;
    --shingle: #8a8270;
  }
  * { margin: 0; padding: 0; box-sizing: border-box; }
  html, body {
    width: 1200px;
    height: 779px;
    overflow: hidden;
    background: var(--page);
  }
  .billboard {
    position: absolute;
    left: 0;
    top: 178px;
    width: 1200px;
    height: 422px;
    display: block;
    font-family: "Montserrat", Arial, sans-serif;
  }
  .headline { font-weight: 800; fill: var(--ink); }
  .headline--red { fill: var(--red); }
  .service { font-weight: 600; font-size: 23px; fill: var(--ink); letter-spacing: 0.3px; }
  .brand-name { font-weight: 600; font-size: 16px; fill: var(--ink); }
  .web-address { font-weight: 700; font-size: 19px; fill: var(--white); letter-spacing: 1.6px; }
  .tick-box { fill: none; stroke: var(--ink); stroke-width: 2; }
  .tick { fill: none; stroke: var(--red); stroke-width: 3; stroke-linecap: round; stroke-linejoin: round; }
</style>
</head>
<body>
<svg class="billboard" viewBox="0 0 1200 422" xmlns="http://www.w3.org/2000/svg">
  <defs>
    <linearGradient id="photoTone" x1="0" y1="0" x2="1" y2="1">
      <stop offset="0" stop-color="#7c7566"/>
      <stop offset="0.45" stop-color="var(--wood)"/>
      <stop offset="1" stop-color="#8c8472"/>
    </linearGradient>
    <linearGradient id="panelTone" x1="0" y1="0" x2="1" y2="0">
      <stop offset="0" stop-color="#ececee"/>
      <stop offset="1" stop-color="var(--white)"/>
    </linearGradient>
  </defs>

  <!-- panel background -->
  <rect class="panel" x="0" y="0" width="1200" height="422" fill="url(#panelTone)"/>
  <polygon class="panel-facet" points="560,0 880,0 1060,240 820,240" fill="#f7f7f8"/>

  <!-- home photo area -->
  <polygon class="house-photo" role="img" aria-label="Photo of a timber-clad house with large arched windows and a new grey-brown shingle roof"
    points="0,0 384,0 608,312 462,422 0,422" fill="url(#photoTone)"/>

  <!-- chevron stripes -->
  <polygon class="stripe-black" points="384,0 396,0 620,312 474,422 462,422 608,312" fill="var(--ink)"/>
  <polygon class="stripe-red" points="405,0 430,0 631,312 500,422 476,422 607,330 612,312" fill="var(--red)"/>

  <!-- logo plate -->
  <polygon class="logo-plate" points="0,31 242,31 262,102 0,102" fill="var(--white)"/>
  <rect class="logo-square" x="16" y="52" width="14" height="14" fill="var(--red)"/>
  <text class="brand-name" x="38" y="62">Harlow Ridge</text>
  <text class="brand-name" x="38" y="82">Construction</text>
  <polygon class="logo-slash" points="222,29 231,29 256,103 247,103" fill="var(--red)"/>
  <polygon class="logo-slash" points="236,29 245,29 270,103 261,103" fill="var(--red)"/>

  <!-- headline -->
  <text class="headline" x="1159" y="71" font-size="39" text-anchor="end">QUALITY YOU</text>
  <text class="headline headline--red" x="1159" y="127" font-size="55" text-anchor="end">DESERVE SERVICE</text>
  <text class="headline" x="1159" y="178" font-size="41" text-anchor="end">YOU CAN COUNT ON</text>

  <!-- services -->
  <g class="service-item">
    <rect class="tick-box" x="694" y="205" width="19" height="19"/>
    <polyline class="tick" points="698,213 704,220 716,203"/>
    <text class="service" x="987" y="224" text-anchor="end">ROOF REPLACEMENT</text>
  </g>
  <g class="service-item">
    <rect class="tick-box" x="1017" y="205" width="19" height="19"/>
    <polyline class="tick" points="1021,213 1027,220 1039,203"/>
    <text class="service" x="1159" y="224" text-anchor="end">GUTTERS</text>
  </g>
  <g class="service-item">
    <rect class="tick-box" x="774" y="240" width="19" height="19"/>
    <polyline class="tick" points="778,248 784,255 796,238"/>
    <text class="service" x="890" y="259" text-anchor="end">SIDING</text>
  </g>
  <g class="service-item">
    <rect class="tick-box" x="920" y="240" width="19" height="19"/>
    <polyline class="tick" points="924,248 930,255 942,238"/>
    <text class="service" x="1159" y="259" text-anchor="end">SNOW REMOVAL</text>
  </g>

  <!-- partner badges -->
  <circle class="badge badge--shingle" cx="844" cy="315" r="18" fill="var(--badge-dark)"/>
  <rect class="badge badge--seal" x="878" y="305" width="26" height="26" fill="var(--badge-dark)"/>
  <rect class="badge badge--accredited" x="925" y="295" width="148" height="49" rx="3" fill="var(--badge-blue)"/>
  <rect class="badge badge--pro" x="1096" y="296" width="40" height="46" rx="3" fill="var(--badge-grey)"/>

  <!-- web address band -->
  <polygon class="web-band" points="654,366 1200,366 1200,406 626,406" fill="var(--ink)"/>
  <polygon class="band-dash" points="586,366 598,366 568,406 556,406" fill="var(--ink)"/>
  <polygon class="band-dash" points="604,366 616,366 586,406 574,406" fill="var(--red)"/>
  <text class="web-address" x="1159" y="393" text-anchor="end">www.<tspan fill="var(--red)">harlowridgeconstruction</tspan>.example</text>
</svg>
</body>
</html>
```